The Lantern Protocol: A Practical Guide for Tending Old Orchards

This will be for both the hard cover and paperback version. A core theme of the book and what we want to cover to convey is the journey or transformation to "happiness". Concepts such as road/pathway, mountain top, sunrise, dark to bright colors, out-of-focus to in-focus, clouds parting, etc., all represent this idea. I am attaching a 1-page book summary for more information. I like the idea of the subtitle being in a gold seal, but that is not necessary. I am open to any designs, but it should at least be conceptually related to the book.

```html
<!DOCTYPE html>
<html lang="en">
<head>
<meta charset="utf-8">
<title>The Lantern Protocol — Book Cover</title>
<link rel="stylesheet" href="https://fonts.googleapis.com/css2?family=Oswald:wght@400;500;600&display=swap">
<style>
  :root {
    --page-bg: #d3e5f8;
    --sky-top: #141c4a;
    --sky-mid: #3a3f95;
    --sky-violet: #7a4fa8;
    --glow-pink: #e77fb8;
    --glow-gold: #ffd25a;
    --ridge-blue: #34507a;
    --mountain-dark: #121826;
    --ink-light: #f4f4f4;
    --title-shadow: rgba(0, 0, 0, 0.75);
  }
  * { margin: 0; padding: 0; box-sizing: border-box; }
  html, body {
    width: 1000px;
    height: 1200px;
    overflow: hidden;
    background: var(--page-bg);
  }
  .book-cover {
    position: absolute;
    left: 123px;
    top: 40px;
    width: 754px;
    height: 1120px;
    overflow: hidden;
    font-family: "Oswald", "Arial Narrow", sans-serif;
    color: var(--ink-light);
  }
  .cover-artwork {
    position: absolute;
    inset: 0;
    background:
      radial-gradient(ellipse 55% 35% at 50% 71%, rgba(255, 210, 90, 0.85), rgba(231, 127, 184, 0.45) 45%, transparent 75%),
      radial-gradient(ellipse 20% 50% at 50% 8%, rgba(231, 127, 184, 0.55), transparent 80%),
      linear-gradient(180deg,
        var(--sky-top) 0%,
        var(--sky-mid) 30%,
        var(--sky-violet) 52%,
        var(--glow-pink) 63%,
        var(--glow-gold) 69%,
        var(--ridge-blue) 72%,
        #1d2438 80%,
        var(--mountain-dark) 100%);
  }
  .cover-title {
    position: absolute;
    left: 0;
    right: 0;
    top: 318px;
    text-align: center;
    font-weight: 600;
    font-size: 124px;
    line-height: 1.06;
    letter-spacing: 1px;
    text-transform: uppercase;
    text-shadow: 4px 5px 6px var(--title-shadow);
  }
  .cover-subtitle {
    position: absolute;
    left: 0;
    right: 0;
    top: 838px;
    text-align: center;
    font-weight: 400;
    font-size: 30px;
    text-shadow: 2px 2px 4px var(--title-shadow);
  }
  .cover-author {
    position: absolute;
    right: 75px;
    top: 944px;
    font-weight: 400;
    font-size: 31px;
    letter-spacing: 0.5px;
    text-shadow: 2px 2px 4px var(--title-shadow);
  }
</style>
</head>
<body>
  <main class="book-cover">
    <div class="cover-artwork" role="img" aria-label="Starry night sky with beams of light pouring down onto a mountain peak at sunrise, a winding glowing path climbing to the summit"></div>
    <h1 class="cover-title">The Lantern<br>Protocol</h1>
    <p class="cover-subtitle">A Practical Guide for Tending Old Orchards</p>
    <p class="cover-author">Miles R. Fenwick</p>
  </main>
</body>
</html>
```